Creative & Professional Business Card for hair salon

We are looking to update our business cards. Our salon is creative, modern, progressive and professional and looking for a design that will reflect this.

```html
<!DOCTYPE html>
<html lang="en">
<head>
<meta charset="utf-8">
<title>Silver Lining Studio — Business Card</title>
<link rel="stylesheet" href="https://fonts.googleapis.com/css2?family=Raleway:wght@400;500&family=Questrial&display=swap">
<style>
  :root {
    --backdrop: #2b2e33;
    --card: #ffffff;
    --slate: #4a6b87;
    --slate-deep: #3f5f7b;
    --teal: #6aa3b8;
    --teal-soft: #8fbcc6;
    --ink-light: #ffffff;
  }
  * { margin: 0; padding: 0; box-sizing: border-box; }
  html, body { width: 1200px; height: 900px; overflow: hidden; }
  body {
    background: var(--backdrop);
    font-family: "Raleway", sans-serif;
    position: relative;
  }
  .card {
    position: absolute;
    top: 300px;
    width: 530px;
    height: 303px;
    background: var(--card);
    border-radius: 26px;
    overflow: hidden;
  }
  .card--front { left: 45px; }
  .card--back  { left: 625px; }

  /* Front */
  .front-ring { position: absolute; inset: 0; }
  .brand-lockup {
    position: absolute;
    left: 0; right: 0; top: 0; bottom: 0;
    display: flex;
    flex-direction: column;
    align-items: center;
    justify-content: center;
    gap: 8px;
    font-family: "Questrial", sans-serif;
    color: var(--slate);
  }
  .brand {
    font-size: 26px;
    font-weight: 400;
    letter-spacing: 0.3px;
    white-space: nowrap;
  }
  .brand-owner {
    font-size: 15px;
    font-weight: 400;
    letter-spacing: 1px;
    white-space: nowrap;
  }

  /* Back */
  .contact-panel {
    position: absolute;
    left: 0; top: 0; bottom: 0;
    width: 310px;
    background: var(--slate);
  }
  .icon-strip {
    position: absolute;
    left: 0; top: 0; bottom: 0;
    width: 50px;
    background: var(--teal);
  }
  .icon-list {
    position: absolute;
    left: 0; top: 30px;
    width: 50px;
    list-style: none;
  }
  .icon-list li {
    height: 27px;
    display: flex;
    align-items: center;
    justify-content: center;
  }
  .contact-list {
    position: absolute;
    left: 66px; top: 30px;
    list-style: none;
    color: var(--ink-light);
    font-size: 12px;
    letter-spacing: 0.2px;
  }
  .contact-list li { height: 27px; line-height: 27px; white-space: nowrap; }
  .panel-notch { position: absolute; left: 296px; top: 86px; }
  .appointment {
    position: absolute;
    left: 342px; top: 88px;
    font-size: 13px;
    letter-spacing: 5px;
    color: var(--slate-deep);
    font-weight: 500;
  }
  .appointment-lines {
    position: absolute;
    left: 330px; top: 134px;
    width: 176px;
  }
  .appointment-lines span {
    display: block;
    height: 2px;
    background: var(--slate);
    margin-bottom: 38px;
  }
</style>
</head>
<body>
  <section class="card card--front" aria-label="Card front">
    <svg class="front-ring" width="530" height="303" viewBox="0 0 530 303" aria-hidden="true">
      <circle cx="265" cy="151" r="136" fill="none" stroke="var(--slate)" stroke-width="12"/>
    </svg>
    <div class="brand-lockup">
      <p class="brand">Silver Lining Studio</p>
      <p class="brand-owner">by Tess Marlow</p>
    </div>
  </section>

  <section class="card card--back" aria-label="Card back">
    <div class="contact-panel">
      <div class="icon-strip"></div>
      <ul class="icon-list" aria-hidden="true">
        <li><svg width="14" height="14" viewBox="0 0 24 24"><path fill="#fff" d="M6.6 10.8a15 15 0 0 0 6.6 6.6l2.2-2.2c.3-.3.7-.4 1-.2 1.1.4 2.3.6 3.6.6.6 0 1 .4 1 1V20c0 .6-.4 1-1 1A17 17 0 0 1 3 4c0-.6.4-1 1-1h3.5c.6 0 1 .4 1 1 0 1.3.2 2.5.6 3.6.1.3 0 .7-.2 1z"/></svg></li>
        <li><svg width="14" height="11" viewBox="0 0 24 18"><rect x="1" y="1" width="22" height="16" rx="1" fill="#fff"/><path d="M1 2l11 8 11-8" fill="none" stroke="var(--teal)" stroke-width="2"/></svg></li>
        <li><svg width="14" height="14" viewBox="0 0 24 24" fill="none" stroke="#fff" stroke-width="2"><circle cx="12" cy="12" r="10"/><ellipse cx="12" cy="12" rx="4.5" ry="10"/><path d="M2 12h20M4 7h16M4 17h16"/></svg></li>
        <li><svg width="8" height="8" viewBox="0 0 10 10"><circle cx="5" cy="5" r="5" fill="#fff"/></svg></li>
        <li><svg width="11" height="14" viewBox="0 0 20 26"><path fill="#fff" d="M10 0a10 10 0 0 0-10 10c0 7 10 16 10 16s10-9 10-16A10 10 0 0 0 10 0zm0 14a4 4 0 1 1 0-8 4 4 0 0 1 0 8z"/></svg></li>
      </ul>
      <ul class="contact-list">
        <li>07 5000 1234</li>
        <li>salon@SilverLiningStudio.com.au</li>
        <li>www.SilverLiningStudio.com.au</li>
        <li>SilverLiningbyTessMarlow</li>
        <li>12/40 Harbour Lane, Coralbay</li>
      </ul>
    </div>
    <svg class="panel-notch" width="28" height="30" viewBox="0 0 28 30" aria-hidden="true">
      <path d="M14 0 C14 8 28 8 28 15 C28 22 14 22 14 30 Z" fill="var(--card)"/>
    </svg>
    <p class="appointment">APPOINTMENT</p>
    <div class="appointment-lines" aria-hidden="true">
      <span></span><span></span><span></span>
    </div>
  </section>
</body>
</html>
```